Help our pizza bases / flat breads fly off the shelves - You'll be seen in supermarkets New Zealand

Packaging design.
We have bought a product that is in desperate need of a complete re-brand. This includes a name, and a package design.
It is an rectangle shaped flat bread that can be used in many ways, and is presented 5 in a pack, in an unprinted flexible formed bottom, with a flat top film applied that is flat and ready to receive your design.
The product is mainly used as a pizza base bought by Mums to feed the family. It is also can be a pre dinner nibble like a pizza bread, and for quick and easy, you can cut one into 3 pieces, and toast in a pop-up toaster, before topping with whatever is in your fridge.
The current name is "Kelmo breads" which is just silly. The brand "Kelmo" needs to change to "Dugald's Flat Breads" or whatever you might suggest. The product name might be "Tavira Pizza Base" or "Tavira Flat bread" as you like.
The look must get consumers to pick up the product and have a closer look. The nature of the graphics should emphasize the versatility and multi-usefulness, so the consumer can imagine what they will do with the product when they get it home. I feel that an informative pack will be better than a beautiful pack to get more sales. I have uploaded pictures showing the product currently in Supermarkets, and also a picture of the current product. Dimensions are 310 x 130mm.
You will need to leave room for: Barcode, Nutritional Panel, Cooking instructions, Storage instructions, Ingredients list and Company contact details - each one say 45 x 45mm or similar.
These details could go on the bottom of the low long side, as this is obscured while on shelf (see photo)
You will also highlight in your design, Preservative Free, 100% Natural, 5 Bases, Made with Olive oil, Hand made, and the variant (Roasted Garlic, or Original)
You will want to highlight the uses like: Pizza base, pizza bread, cut toast and top or similar.

```html
<!DOCTYPE html>
<html lang="en">
<head>
<meta charset="utf-8">
<title>Dugald's Flat Breads – Tavira Pizza Base labels</title>
<link rel="stylesheet" href="https://fonts.googleapis.com/css2?family=Cinzel:wght@700&display=swap">
<style>
  :root {
    --page: #ffffff;
    --ink-black: #0b0b0b;
    --ink-dark: #1a1a1a;
    --frame-white: #f2f2f2;
    --text-light: #ffffff;
    --text-soft: #bdbdbd;
    --flag-green: #1d8f3a;
    --flag-green-deep: #0b5a22;
    --flag-silver: #e4e4e4;
    --flag-silver-deep: #9a9a9a;
    --flag-red: #c8161e;
    --flag-red-deep: #6e0a0e;
    --pizza-red: #b5563d;
    --pizza-green: #5f7a3a;
    --cheese: #e6dcc4;
    --cheese-shade: #b9a98a;
    --dough: #e9e6d2;
    --dough-shade: #d5d1b6;
  }
  * { box-sizing: border-box; margin: 0; padding: 0; }
  html, body { width: 1200px; height: 1200px; overflow: hidden; background: var(--page); }
  .sheet {
    width: 1200px; height: 1200px;
    display: flex; flex-direction: column; align-items: center; justify-content: center; gap: 100px;
  }
  .label {
    position: relative;
    width: 1000px; height: 420px;
    border-radius: 14px;
    overflow: hidden;
    font-family: "Cinzel", serif;
    font-weight: 700;
  }
  .label--black { background: var(--ink-black); color: var(--text-light); }
  .label--black::before {
    content: ""; position: absolute; inset: 14px;
    border: 3px solid var(--frame-white); border-radius: 10px;
  }
  .label--flag {
    color: var(--ink-dark);
    background: linear-gradient(90deg,
      var(--flag-green-deep) 0%, var(--flag-green) 12%, var(--flag-green-deep) 24%, var(--flag-green) 33.3%,
      var(--flag-silver) 33.3%, var(--flag-silver-deep) 45%, #fafafa 55%, var(--flag-silver-deep) 66.6%,
      var(--flag-red) 66.6%, var(--flag-red-deep) 78%, var(--flag-red) 88%, var(--flag-red-deep) 100%);
  }
  .brand {
    position: absolute; top: 40px; left: 0; right: 0; text-align: center;
    font-size: 24px; letter-spacing: 2px; line-height: 1;
  }
  .label--black .brand { color: var(--text-soft); }
  .title {
    position: absolute; top: 84px; left: 0; right: 0; text-align: center;
    font-size: 54px; font-weight: 700; line-height: 1; letter-spacing: 1px;
  }
  .title-plate {
    display: inline-block; padding: 6px 22px;
  }
  .label--flag .title-plate,
  .label--flag .brand-plate,
  .label--flag .count-plate {
    background: var(--flag-silver);
    border-radius: 4px;
  }
  .brand-plate { display: inline-block; padding: 4px 14px; }
  .windows {
    position: absolute; top: 180px; left: 80px; right: 80px; height: 160px;
    display: flex; gap: 24px;
  }
  .window { flex: 1; border-radius: 2px; }
  .window--pizza { background: radial-gradient(circle at 40% 45%, var(--pizza-green) 0%, var(--pizza-red) 45%, #9c4530 100%); }
  .window--cheese { background: radial-gradient(circle at 50% 50%, var(--cheese) 0%, var(--cheese-shade) 100%); }
  .window--bread { background: radial-gradient(circle at 45% 40%, var(--dough) 0%, var(--dough-shade) 100%); }
  .count {
    position: absolute; top: 356px; left: 0; right: 0; text-align: center;
    font-size: 24px; letter-spacing: 1px; line-height: 1;
  }
  .count-plate { display: inline-block; padding: 6px 16px; }
</style>
</head>
<body>
<main class="sheet">

  <section class="label label--black">
    <p class="brand"><span class="brand-plate">Dugald's Flat Breads</span></p>
    <h1 class="title"><span class="title-plate">Tavira Pizza Base</span></h1>
    <div class="windows">
      <div class="window window--pizza" role="img" aria-label="Topped pizza with tomato and fresh herbs"></div>
      <div class="window window--cheese" role="img" aria-label="Flat bread covered in grated cheese"></div>
      <div class="window window--bread" role="img" aria-label="Clear window showing the plain flat bread"></div>
    </div>
    <p class="count"><span class="count-plate">5 Garlic Flat Breads</span></p>
  </section>

  <section class="label label--flag">
    <p class="brand"><span class="brand-plate">Dugald's Flat Breads</span></p>
    <h1 class="title"><span class="title-plate">Tavira Pizza Base</span></h1>
    <div class="windows">
      <div class="window window--pizza" role="img" aria-label="Topped pizza with tomato and fresh herbs"></div>
      <div class="window window--cheese" role="img" aria-label="Flat bread covered in grated cheese"></div>
      <div class="window window--bread" role="img" aria-label="Clear window showing the plain flat bread"></div>
    </div>
    <p class="count"><span class="count-plate">5 Garlic Flat Breads</span></p>
  </section>

</main>
</body>
</html>
```